Postcard design to acquire new clients for my Property Management Company

I'm looking for a postcard design that I can send to prospective clients detailing information about my company and services.
Postcard should be eye catching and contain information from www.brightkeyrentals-example.com. I've provided a few screen shots for the most important information and my logo.
Target Market(s)
Real Estate
Industry/Entity Type
Real Estate
Font styles to use
Sans Serif
Requirements
Must have
- Must be eye catching!! this will be a direct mail piece - I'd like for the card to be read and not tossed in the trash immediately.
Design que from the logo.
A place to write / print the receipts name and address.
our physical address - 2287 Marble Lane, Lubbock, TX 79555.
Should not have
- the contact information on the business card is not accurate - please use info from website.

```html
<!DOCTYPE html>
<html lang="en">
<head>
<meta charset="utf-8">
<title>BrightKey Rentals – Postcard</title>
<link href="https://fonts.googleapis.com/css2?family=Montserrat:wght@400;500;600;700;800&display=swap" rel="stylesheet">
<style>
  :root{
    --navy:#0f4186;
    --navy-deep:#0b3470;
    --grey-stripe:#a9a9ab;
    --panel:#efeff0;
    --page:#cac9cb;
    --ink:#3d3d3f;
    --white:#ffffff;
  }
  *{box-sizing:border-box;margin:0;padding:0}
  html,body{width:1200px;height:2830px;overflow:hidden}
  body{background:var(--page);font-family:'Montserrat',sans-serif;color:var(--ink);position:relative}

  .card{position:absolute;left:93px;width:1013px;background:var(--white);overflow:hidden}
  .card--front{top:1045px;height:720px}
  .card--back{top:1885px;height:722px}
  .shape-layer{position:absolute;inset:0;width:100%;height:100%}

  /* front */
  .brand{position:absolute;color:var(--navy);font-weight:700;letter-spacing:.14em;text-transform:uppercase;line-height:1}
  .front__brand{left:60px;top:42px}
  .front__brand .brand-main{font-size:46px;display:block}
  .front__brand .brand-sub{font-size:20px;display:block;margin-top:12px;letter-spacing:.2em}

  .hero-photo{position:absolute;left:0;top:0;width:1013px;height:333px;
    clip-path:polygon(614px 0,1013px 0,1013px 333px,541px 333px);
    background:linear-gradient(120deg,#d9dbe0 0%,#eef0f3 35%,#e9d3c6 55%,#c7644a 72%,#e8e8ea 88%,#bfc3c8 100%)}
  .hero-copy{position:absolute;left:55px;top:165px;color:var(--white)}
  .hero-copy h1{font-size:28px;font-weight:800;line-height:34px;letter-spacing:.01em}
  .hero-copy .rule{width:365px;height:2px;background:rgba(255,255,255,.75);margin:22px 0 14px}
  .hero-copy p{font-size:15px;line-height:17px;font-weight:500}

  .plan{position:absolute;width:265px;background:var(--white);box-shadow:0 2px 6px rgba(0,0,0,.22);text-align:center;padding-top:16px}
  .plan--lease{left:67px;top:345px;height:322px}
  .plan--full{left:377px;top:343px;height:354px;padding-top:12px}
  .plan--premium{left:677px;top:345px;height:322px}
  .plan__name{color:var(--navy);font-weight:700;font-size:15px;line-height:17px}
  .plan__tag{font-size:14px;line-height:17px}
  .plan__rate{color:var(--navy);font-weight:800;font-size:40px;line-height:48px;margin-top:4px}
  .plan__basis{font-size:12px;line-height:14px}
  .plan__list{list-style:none;margin-top:14px;font-size:12.5px;line-height:24px}
  .plan__cta{display:inline-block;background:var(--navy);color:var(--white);font-weight:700;font-size:12px;letter-spacing:.03em;padding:2px 10px;border-radius:10px;margin-top:10px}
  .plan--premium .plan__cta{margin-top:46px}
  .front__base{position:absolute;left:0;bottom:0;width:100%;height:17px;background:var(--grey-stripe)}

  /* back */
  .services-head{position:absolute;left:45px;top:38px}
  .services-head h2{color:var(--navy);font-size:25px;font-weight:800;letter-spacing:.01em}
  .services-head p{font-size:14px;margin-top:4px}
  .service{position:absolute;width:200px;text-align:center}
  .service svg{display:block;margin:0 auto;height:30px}
  .service h3{color:var(--navy);font-size:13px;font-weight:700;margin-top:4px;line-height:16px}
  .service p{font-size:10.5px;line-height:12px;margin-top:3px}
  .col-a{left:38px}
  .col-b{left:268px}

  .contact{position:absolute;left:0;top:610px;height:112px;color:var(--white)}
  .contact__label{position:absolute;left:24px;top:30px;width:148px;text-align:right;font-weight:800;font-size:21px;line-height:26px}
  .contact__divider{position:absolute;left:186px;top:22px;width:2px;height:70px;background:var(--white)}
  .contact__lines{position:absolute;left:202px;top:24px;font-size:14px;line-height:21px;white-space:nowrap}

  .mail__brand{left:592px;top:95px}
  .mail__brand .brand-main{font-size:23px;display:block}
  .mail__brand .brand-sub{font-size:11px;display:block;margin-top:4px;letter-spacing:.2em}
  .stamp-box{position:absolute;left:862px;top:40px;width:98px;height:120px;border:2px solid #333}
  .address-line{position:absolute;left:617px;width:333px;height:1px;background:#555}
</style>
</head>
<body>

<section class="card card--front" aria-label="Postcard front">
  <div class="hero-photo" role="img" aria-label="Photo of a hand reviewing printed financial charts beside a red model apartment building"></div>
  <svg class="shape-layer" viewBox="0 0 1013 720" aria-hidden="true">
    <polygon points="0,127 498,127 453,333 0,333" fill="var(--navy)"/>
    <polygon points="532,0 568,0 495,333 459,333" fill="var(--grey-stripe)"/>
    <polygon points="575,0 607,0 534,333 502,333" fill="var(--navy)"/>
  </svg>
  <div class="brand front__brand"><span class="brand-main">BrightKey</span><span class="brand-sub">Rentals</span></div>
  <div class="hero-copy">
    <h1>PROPERTY MANAGEMENT<br>ACROSS LUBBOCK, TX</h1>
    <div class="rule"></div>
    <p>Maximize your financial returns with support<br>from our rental specialists</p>
  </div>

  <div class="plan plan--lease">
    <div class="plan__name">Lease Only</div>
    <div class="plan__tag">- You Just Need Tenants -</div>
    <div class="plan__rate">9%</div>
    <div class="plan__basis">of annual lease</div>
    <ul class="plan__list">
      <li>Professional Photography</li><li>Marketing &amp; Advertising</li><li>Property Showings</li>
      <li>Tenant Screening &amp; Qualifications</li><li>Lease Execution</li><li>Move In Coordination</li>
    </ul>
    <span class="plan__cta">GET STARTED</span>
  </div>
  <div class="plan plan--full">
    <div class="plan__name">Full Service</div>
    <div class="plan__tag">-Our Most Popular-</div>
    <div class="plan__rate">10%</div>
    <div class="plan__basis">of monthly rent</div>
    <ul class="plan__list">
      <li>Includes Leasing Service</li><li>24/7 Emergency Response</li><li>Move In &amp; Out Inspections</li>
      <li>Professional Lease Enforcement</li><li>Schedule &amp; Oversee all Repairs</li><li>Pay all Invoices</li>
      <li>Monthly &amp; Year End Statements</li><li>Annual Market Rent Analysis</li>
    </ul>
    <span class="plan__cta">GET STARTED</span>
  </div>
  <div class="plan plan--premium">
    <div class="plan__name">Premium Service</div>
    <div class="plan__tag">- Our Premier Service -</div>
    <div class="plan__rate">12%</div>
    <div class="plan__basis">of monthly rent</div>
    <ul class="plan__list">
      <li>Includes Full Service Features</li><li>Professional Video Marketing</li>
      <li>Home Warranty Coordination</li><li>Tenant Retention Program</li>
    </ul>
    <span class="plan__cta">GET STARTED</span>
  </div>
  <div class="front__base"></div>
</section>

<section class="card card--back" aria-label="Postcard back">
  <svg class="shape-layer" viewBox="0 0 1013 722" aria-hidden="true">
    <polygon points="0,105 471,105 599,610 0,610" fill="var(--panel)"/>
    <polygon points="445,0 482,0 531,340" fill="var(--navy)"/>
    <polygon points="531,340 621,610 599,610" fill="var(--grey-stripe)"/>
    <polygon points="0,610 599,610 627,722 0,722" fill="var(--navy)"/>
  </svg>

  <div class="services-head">
    <h2>DISCOVER OUR SERVICES</h2>
    <p>We offer full-service property management solutions</p>
  </div>

  <div class="service col-a" style="top:118px">
    <svg viewBox="0 0 32 28" width="32"><path d="M16 2 1 15h4v11h8v-7h6v7h8V15h4z" fill="var(--navy)"/></svg>
    <h3>Property Marketing</h3>
    <p>Tired of waiting for weeks on end, hoping to find a new tenant? Let us take over your marketing for you and we'll find a qualified renter quickly.</p>
  </div>
  <div class="service col-b" style="top:118px">
    <svg viewBox="0 0 40 28" width="40"><circle cx="13" cy="8" r="6" fill="var(--navy)"/><circle cx="28" cy="8" r="6" fill="var(--navy)"/><path d="M2 27c0-8 5-12 11-12s11 4 11 12z M20 27c0-6 2-11 8-11s10 4 10 11z" fill="var(--navy)"/></svg>
    <h3>Tenant Screening</h3>
    <p>We don't just find someone to rent your home—we find the best renters. We screen all applications using fair housing guidelines to protect you.</p>
  </div>
  <div class="service col-a" style="top:236px">
    <svg viewBox="0 0 20 34" width="20"><text x="10" y="29" text-anchor="middle" font-family="Montserrat,sans-serif" font-weight="800" font-size="34" fill="var(--navy)">$</text></svg>
    <h3>Rent Collection</h3>
    <p>Stop guessing when you'll receive your rental earnings every month and say hello to consistent payments. We keep your tenants current.</p>
  </div>
  <div class="service col-b" style="top:236px">
    <svg viewBox="0 0 34 34" width="34"><path d="M4 31 20 15l3 3L7 34z" fill="var(--navy)"/><path d="M14 9l8-7 10 4-4 3 3 3-5 5-3-3-4 4-5-5z" fill="var(--navy)"/></svg>
    <h3>Maintenance</h3>
    <p>Still scrambling to respond to repair requests every time you receive a tenant call? Let us coordinate repair work on your behalf!</p>
  </div>
  <div class="service col-a" style="top:353px">
    <svg viewBox="0 0 32 32" width="32"><circle cx="13" cy="13" r="9" fill="none" stroke="var(--navy)" stroke-width="4"/><path d="M19 19l10 10" stroke="var(--navy)" stroke-width="5" stroke-linecap="round"/></svg>
    <h3>Property Inspections</h3>
    <p>Inspections form an important part of our proactive property management approach. We visit every home in our portfolio regularly.</p>
  </div>
  <div class="service col-b" style="top:353px">
    <svg viewBox="0 0 34 28" width="34"><path d="M3 2v24h29" fill="none" stroke="var(--navy)" stroke-width="2.5"/><rect x="8" y="14" width="3" height="10" fill="var(--navy)"/><rect x="14" y="8" width="3" height="16" fill="var(--navy)"/><rect x="20" y="11" width="3" height="13" fill="var(--navy)"/><rect x="26" y="5" width="3" height="19" fill="var(--navy)"/></svg>
    <h3>Financial Reporting</h3>
    <p>Keep a handle on your real estate performance. We generate monthly statements so you can review income &amp; expenses at a moment's notice.</p>
  </div>
  <div class="service col-a" style="top:472px">
    <svg viewBox="0 0 28 32" width="28"><path d="M14 1 2 6v9c0 8 5 13 12 16 7-3 12-8 12-16V6z" fill="var(--navy)"/><path d="M14 5v22c-5-2-8-6-8-12V9z" fill="var(--white)"/></svg>
    <h3>Evictions</h3>
    <p>When things go wrong inside your rental home, rest easy with the experts on your side. We will handle evictions for you &amp; find new renters when its over.</p>
  </div>
  <div class="service col-b" style="top:472px">
    <svg viewBox="0 0 36 30" width="36"><path d="M18 2v24M8 28h20M4 7h28" stroke="var(--navy)" stroke-width="2.5" fill="none"/><path d="M9 7 3 19h12zM27 7l-6 12h12z" fill="none" stroke="var(--navy)" stroke-width="2"/><path d="M3 19a6 4 0 0 0 12 0zM21 19a6 4 0 0 0 12 0z" fill="var(--navy)"/></svg>
    <h3>Legal Guidance</h3>
    <p>Don't accidentally violate one of the many ordinances and housing laws governing your relationship with your tenants. Let us keep you compliant.</p>
  </div>

  <div class="contact">
    <div class="contact__label">CONTACT<br>OUR TEAM</div>
    <div class="contact__divider"></div>
    <div class="contact__lines">Give us a call now: (806) 555-0147<br>Email us: info@brightkeyrentals-example.com<br>2287 Marble Lane, Lubbock, TX 79555</div>
  </div>

  <div class="brand mail__brand"><span class="brand-main">BrightKey</span><span class="brand-sub">Rentals</span></div>
  <div class="stamp-box" aria-label="Stamp area"></div>
  <div class="address-line" style="top:278px"></div>
  <div class="address-line" style="top:344px"></div>
  <div class="address-line" style="top:417px"></div>
</section>

</body>
</html>
```